Marisol transparent business card

I would like to have a transparent business card created.
A simple yet classy card with
Website www.MarisolPennywhite.com
Phone # 555-417-2936
I would like my full photo on the card as well as my logo.

Target Market(s)

The business card will be printed on transparent card stock.
Www.MarisolPennywhite.com
Phone 555-417-2936
I would like my pic on the card and my logo
Author, Speaker, & Wealth architect

Industry/Entity Type

Business

Contact Information for Business Card

Www.MarisolPennywhite.com
Phone 555-417-2936

Font styles to use
Serif
Decorative
Script

Requirements
Must have
• The business card will be printed on transparent card stock.
• Www.MarisolPennywhite.com
• Phone 555-417-2936
• I would like my pic on the card and my logo
• Author, Speaker, & Wealth architect
Nice to have
• If I could have the tattoo on my pic blurred out or airbrushed over

```html
<!DOCTYPE html>
<html lang="en">
<head>
<meta charset="utf-8">
<title>Marisol Pennywhite — Transparent Business Card</title>
<link rel="stylesheet" href="https://fonts.googleapis.com/css2?family=Great+Vibes&family=Cinzel:wght@400&family=Open+Sans:wght@400&display=swap">
<style>
  :root {
    --page-bg: #e8e5e2;
    --card-clear: rgba(255, 255, 255, 0.78);
    --card-clear-edge: rgba(240, 236, 236, 0.9);
    --band-black: #050505;
    --gold: #c9a13a;
    --gold-light: #e6c766;
    --ink-grey: #4a4a4a;
    --white: #ffffff;
    --photo-dark: #1b1614;
    --photo-mid: #5a4238;
    --photo-light: #d9d4d0;
  }
  * { margin: 0; padding: 0; box-sizing: border-box; }
  html, body { width: 1200px; height: 900px; overflow: hidden; }
  body { background: var(--page-bg); position: relative; font-family: "Open Sans", Arial, sans-serif; }

  .card {
    position: absolute;
    overflow: hidden;
    background: linear-gradient(180deg, var(--card-clear) 0%, var(--card-clear-edge) 100%);
    box-shadow: 0 6px 18px rgba(0,0,0,0.12);
  }
  .card--front { left: 238px; top: 61px; width: 555px; height: 344px; }
  .card--back  { left: 457px; top: 518px; width: 560px; height: 343px; }

  .contact-band { position: absolute; left: 0; right: 0; bottom: 0; top: 219px; background: var(--band-black); }

  .portrait {
    position: absolute;
    background: linear-gradient(180deg, var(--photo-light) 0%, var(--photo-mid) 22%, var(--photo-dark) 45%, var(--photo-dark) 100%);
    border-radius: 60px 60px 0 0;
  }
  .card--front .portrait { left: 0; top: 0; width: 172px; height: 344px; }
  .card--back .portrait { right: 0; top: 0; width: 180px; height: 218px; opacity: 0.7; }

  .brand { position: absolute; text-align: center; }
  .card--front .brand { left: 234px; top: 58px; width: 300px; }
  .card--back .brand { left: 20px; top: 58px; width: 300px; transform: scaleX(-1); opacity: 0.75; }

  .brand__mark {
    display: block; margin: 0 auto 6px;
    width: 72px; height: 72px; border-radius: 50%;
    border: 3px solid var(--gold);
  }
  .brand__name {
    font-family: "Great Vibes", cursive;
    font-size: 30px; line-height: 1.1;
    color: var(--gold);
    word-spacing: 4px;
    white-space: nowrap;
  }
  .brand__tagline {
    font-family: "Cinzel", serif;
    font-size: 9px; letter-spacing: 0.3px;
    color: var(--ink-grey);
    margin-top: 1px;
    white-space: nowrap;
  }

  .contact-list {
    position: absolute; right: 40px; top: 242px;
    list-style: none; text-align: right;
    color: var(--white); font-size: 14.5px;
  }
  .contact-list li { display: flex; justify-content: flex-end; align-items: center; gap: 7px; line-height: 21px; }
  .contact-list .roles { margin-top: 11px; }
  .contact-icon { width: 11px; height: 11px; }

  .back-web {
    position: absolute; left: 0; right: 18px; top: 276px;
    text-align: center; color: var(--white);
    font-size: 12.5px; letter-spacing: 0.2px;
  }
</style>
</head>
<body>

  <section class="card card--front" aria-label="Business card front">
    <div class="contact-band"></div>
    <div class="portrait" role="img" aria-label="Full-length photo of Marisol in a black dress, arms crossed"></div>

    <div class="brand">
      <span class="brand__mark"></span>
      <div class="brand__name">Marisol Pennywhite</div>
      <div class="brand__tagline">BUILD YOUR LEGACY WITH INTENT, NO LIMITS</div>
    </div>

    <ul class="contact-list">
      <li>555-417-2936
        <svg class="contact-icon" viewBox="0 0 12 12" aria-hidden="true"><path fill="#e6c766" d="M1 4c0-2 2-3 5-3s5 1 5 3v1H8V3.6H4V5H1zM3 6h6l1.5 5h-9z"/><circle cx="6" cy="8.3" r="1.2" fill="#050505"/></svg>
      </li>
      <li>Www.MarisolPennywhite.com
        <svg class="contact-icon" viewBox="0 0 12 12" aria-hidden="true"><rect x="1" y="2.5" width="10" height="7" fill="#e6c766"/><path d="M1 2.5l5 4 5-4" fill="none" stroke="#050505" stroke-width="0.9"/></svg>
      </li>
      <li class="roles">Author | Speaker | Wealth architect</li>
    </ul>
  </section>

  <section class="card card--back" aria-label="Business card back">
    <div class="contact-band"></div>
    <div class="portrait" role="img" aria-label="Front photo of Marisol seen through the clear card"></div>

    <div class="brand">
      <span class="brand__mark"></span>
      <div class="brand__name">Marisol Pennywhite</div>
      <div class="brand__tagline">BUILD YOUR LEGACY WITH INTENT, NO LIMITS</div>
    </div>

    <p class="back-web">WWW.MARISOLPENNYWHITE.COM</p>
  </section>

</body>
</html>
```